App for Lawyers & Accountants needs 'Professional' Styling

We want to style our app to convey a 'Professional' appearance. It's used by Lawyers, Accountants, Doctors etc. who take their work very seriously.

We currently trying to follow keystrel layout guidelines, but we find our app looks very bland. I've uploaded a screenshot of our current app, and two mock-ups of more stylized versions, but we're not happy with those mock-ups.

We'd like to see alternate designs for those two mock-ups, that look much more professional.

The specific elements we'd like to improve/focus on are:
* Colour of the top and left nav bars
* Appearance of the left nav, size, icons spacing
* Appearance of the buttons on the top right, so the user knows they are buttons they can press
* Spacing of the dashboard, background colour and spacing, colour/layout of the 'overdue' and 'todo' accordion headings in the 'my tasks' section.
* List view background grey, to be consistent with dashboard, but unobtrusive
* List view tabs to be obvious as tabs, but 'saved searches', filters and the export icon to still be associated with the data displayed, but it should be obvious to the user that those are different buttons, not just more tabs. (I.e. the filters button opens a panel below it that allows the user to filter the data in the list.)
* General appearance of the popup menu when you push the 'add' button on the top right

However, despite those specifics I'm sure it's all the subtle elements of the design that make a big difference.

Our brand colour is 1D4F91, and we use A20067 as a secondary colour in print media, (although it doesn't seem to work to well within the app.) Our brand font is signika. We'd like the designs to be based on those colours & font.

Target Market(s)

Professional people, Lawyers, Accountants, Doctors etc.

Font styles to use
Sans Serif
Other font styles liked:
• Signika

Colors
0255a3

Requirements
Must have
• The most 'Professional' experience/quality possible. Think the quality & brand image of vantrel desk, but taken to a higher level.
• An example/mock-up of the dashboard, list view and 'add' item popup menu
• Display the dashboard cards with the same information as our mock-ups - the information there is important and we don't have any extra cards to add (in the near term)
Nice to have
• Various colour combinations for the top and left nav bars, based on our primary blue brand colour, and perhaps some shade of dark grey.

```html
<!DOCTYPE html>
<html lang="en">
<head>
<meta charset="utf-8">
<title>Dashboard</title>
<link rel="stylesheet" href="https://fonts.googleapis.com/css2?family=Signika:wght@300;400;500;600&display=swap">
<style>
  :root {
    --brand: #1d4f91;
    --brand-dark: #173f74;
    --accent: #a20067;
    --orange: #f5a623;
    --green: #7cb342;
    --sky: #1e9be0;
    --page: #edf0f2;
    --card: #ffffff;
    --line: #e3e7eb;
    --text: #3a3f45;
    --muted: #6b737b;
    --stat: #f1f3f5;
  }
  * { box-sizing: border-box; margin: 0; padding: 0; }
  html, body { width: 1200px; height: 478px; overflow: hidden; }
  body {
    font-family: "Signika", "Segoe UI", sans-serif;
    background: var(--page);
    color: var(--text);
    position: relative;
  }
  .sidebar {
    position: absolute; left: 0; top: 0; width: 42px; height: 478px;
    background: var(--brand);
  }
  .sidebar .brand-name {
    position: absolute; top: 11px; left: 0; width: 42px; text-align: center;
    color: #fff; font-size: 10px; font-weight: 500;
  }
  .nav-item {
    position: absolute; left: 0; width: 42px; height: 26px;
    display: flex; align-items: center; justify-content: center;
  }
  .nav-item.active { background: rgba(255,255,255,.08); box-shadow: inset 2px 0 0 #8fb6ea; }
  .nav-badge {
    position: absolute; left: 23px; top: 1px; min-width: 12px; height: 12px;
    border-radius: 6px; font-size: 7px; color: #fff; line-height: 12px; text-align: center;
  }
  .topbar {
    position: absolute; left: 42px; top: 0; right: 0; height: 36px;
    background: #fff; border-bottom: 1px solid var(--line);
  }
  .search { position: absolute; left: 24px; top: 11px; display: flex; align-items: center; gap: 8px; font-size: 10px; color: var(--muted); }
  .add-button {
    position: absolute; left: 907px; top: 9px; width: 48px; height: 18px; border-radius: 9px;
    background: #eef0f2; font-size: 10px; color: var(--muted);
    display: flex; align-items: center; justify-content: center; gap: 4px; border: 0; font-family: inherit;
  }
  .icon-button {
    position: absolute; top: 9px; width: 18px; height: 18px; border-radius: 50%;
    display: flex; align-items: center; justify-content: center;
  }
  .icon-button.clock { left: 971px; background: #eef0f2; }
  .icon-button.bell { left: 1005px; background: #eef0f2; }
  .bell-badge {
    position: absolute; left: 9px; top: -5px; width: 12px; height: 12px; border-radius: 50%;
    background: var(--accent); color: #fff; font-size: 7px; line-height: 12px; text-align: center;
  }
  .user { position: absolute; left: 1052px; top: 12px; font-size: 10px; color: var(--text); display: flex; gap: 4px; align-items: center; }
  .avatar { position: absolute; left: 1120px; top: 8px; }
  .page-header {
    position: absolute; left: 42px; top: 37px; right: 0; height: 41px;
    background: #fff; border-bottom: 1px solid var(--line);
  }
  .page-header h1 { position: absolute; left: 24px; top: 11px; font-size: 14px; font-weight: 400; color: var(--text); }
  .card { position: absolute; background: var(--card); }
  .card-title {
    height: 30px; padding: 8px 14px 0; font-size: 11.5px; font-weight: 500; color: var(--text);
    border-bottom: 1px solid var(--line);
  }
  .tasks { left: 66px; top: 96px; width: 282px; height: 234px; }
  .accordion-head {
    position: absolute; left: 14px; width: 254px; height: 25px; color: #fff;
    font-size: 10.5px; display: flex; align-items: center; padding: 0 12px;
  }
  .accordion-head.overdue { top: 44px; background: var(--brand); }
  .accordion-head.todo { top: 195px; background: var(--accent); }
  .accordion-head .count {
    margin-left: auto; width: 13px; height: 13px; border-radius: 50%; background: var(--orange);
    font-size: 7px; line-height: 13px; text-align: center; margin-right: 10px;
  }
  .task-list {
    position: absolute; left: 14px; top: 69px; width: 254px; height: 126px;
    border-left: 1px solid var(--line); border-right: 1px solid var(--line);
  }
  .task { position: absolute; left: 12px; right: 12px; }
  .task-name { font-size: 10px; color: var(--brand); }
  .task-meta { display: flex; align-items: center; gap: 6px; margin-top: 4px; font-size: 8px; color: var(--muted); }
  .task-meta .date { margin-left: auto; }
  .time { left: 374px; top: 96px; width: 436px; height: 311px; }
  .stat {
    position: absolute; top: 40px; height: 39px; background: var(--stat);
    text-align: center; padding-top: 5px;
  }
  .stat-label { font-size: 9.5px; color: var(--muted); text-transform: uppercase; }
  .stat-value { font-size: 17px; color: var(--text); line-height: 1.1; }
  .chart { position: absolute; left: 0; top: 0; }
  .matters { left: 835px; top: 96px; width: 282px; height: 234px; }
  .matter { position: absolute; left: 14px; right: 14px; display: flex; gap: 6px; }
  .matter-name { font-size: 10px; color: var(--brand); line-height: 1.1; }
  .stamp { font-size: 7.5px; color: var(--muted); margin-top: 4px; }
  .documents { left: 66px; top: 342px; width: 282px; height: 116px; }
  .document { position: absolute; left: 14px; display: flex; gap: 5px; }
</style>
</head>
<body>
  <nav class="sidebar" aria-label="Main navigation">
    <div class="brand-name">Lexa</div>
    <div class="nav-item" style="top:39px">
      <svg width="10" height="10" viewBox="0 0 10 10"><path d="M3 1l4 4-4 4" fill="none" stroke="#8fb6ea" stroke-width="1.6"/></svg>
    </div>
    <div class="nav-item active" style="top:69px">
      <svg width="14" height="14" viewBox="0 0 14 14" fill="none" stroke="#fff" stroke-width="1.2"><circle cx="7" cy="7" r="5.5"/><path d="M7 7l2.5-2.5M4 10h6"/></svg>
    </div>
    <div class="nav-item" style="top:97px">
      <svg width="14" height="14" viewBox="0 0 14 14" fill="none" stroke="#fff" stroke-width="1.2"><path d="M3 10V6a4 4 0 0 1 8 0v4l1 1H2z"/><path d="M6 12.5h2"/></svg>
      <span class="nav-badge" style="background:var(--orange)">27</span>
    </div>
    <div class="nav-item" style="top:125px">
      <svg width="14" height="14" viewBox="0 0 14 14" fill="none" stroke="#fff" stroke-width="1.2"><rect x="1.5" y="4" width="11" height="8" rx="1"/><path d="M5 4V2.5h4V4"/></svg>
      <span class="nav-badge" style="background:var(--green)">4</span>
    </div>
    <div class="nav-item" style="top:153px">
      <svg width="14" height="14" viewBox="0 0 14 14" fill="none" stroke="#fff" stroke-width="1.2"><path d="M9 4l-5 5a1.5 1.5 0 0 0 2 2l6-6a2.5 2.5 0 0 0-3.5-3.5L2.5 7.5"/></svg>
      <span class="nav-badge" style="background:var(--sky)">2</span>
    </div>
    <div class="nav-item" style="top:184px">
      <svg width="14" height="14" viewBox="0 0 14 14" fill="none" stroke="#fff" stroke-width="1.2"><circle cx="7" cy="7" r="5.5"/><path d="M7 4v3"/></svg>
    </div>
    <div class="nav-item" style="top:213px">
      <svg width="14" height="14" viewBox="0 0 14 14" fill="none" stroke="#fff" stroke-width="1.2"><circle cx="7" cy="4.5" r="3"/><path d="M1.5 13a5.5 5.5 0 0 1 11 0"/></svg>
    </div>
    <div class="nav-item" style="top:270px">
      <svg width="14" height="14" viewBox="0 0 14 14" fill="none" stroke="#fff" stroke-width="1.2"><circle cx="7" cy="7" r="2"/><path d="M7 1v2M7 11v2M1 7h2M11 7h2M2.8 2.8l1.4 1.4M9.8 9.8l1.4 1.4M2.8 11.2l1.4-1.4M9.8 4.2l1.4-1.4"/></svg>
    </div>
  </nav>

  <header class="topbar">
    <div class="search">
      <svg width="12" height="12" viewBox="0 0 12 12" fill="none" stroke="#555" stroke-width="1.3"><circle cx="5" cy="5" r="4"/><path d="M8 8l3.5 3.5"/></svg>
      Search
    </div>
    <button class="add-button">
      <svg width="9" height="9" viewBox="0 0 9 9" stroke="#444" stroke-width="1.6"><path d="M4.5 0v9M0 4.5h9"/></svg>Add
    </button>
    <div class="icon-button clock">
      <svg width="11" height="11" viewBox="0 0 11 11" fill="none" stroke="#555" stroke-width="1.1"><circle cx="5.5" cy="5.5" r="4.6"/><path d="M5.5 3v2.7l1.8 1"/></svg>
    </div>
    <div class="icon-button bell">
      <svg width="11" height="11" viewBox="0 0 11 11" fill="none" stroke="#555" stroke-width="1.1"><path d="M2.5 8V5a3 3 0 0 1 6 0v3l.8.8H1.7z"/><path d="M4.5 10h2"/></svg>
      <span class="bell-badge">27</span>
    </div>
    <div class="user">Mara Quill
      <svg width="7" height="5" viewBox="0 0 7 5" fill="none" stroke="#444" stroke-width="1.2"><path d="M.5.5l3 3 3-3"/></svg>
    </div>
    <svg class="avatar" width="22" height="22" viewBox="0 0 22 22" fill="none">
      <circle cx="10" cy="10" r="9" fill="#f5e6ef"/>
      <circle cx="10" cy="8" r="3.3" stroke="var(--accent)" stroke-width="1.2"/>
      <path d="M4.5 16a5.5 5.5 0 0 1 11 0" stroke="var(--accent)" stroke-width="1.2"/>
      <circle cx="17" cy="17" r="2.5" fill="#3cb44b" stroke="#fff"/>
    </svg>
  </header>

  <div class="page-header"><h1>Dashboard</h1></div>

  <section class="card tasks">
    <div class="card-title">My Tasks</div>
    <div class="accordion-head overdue">Overdue<span class="count">3</span>
      <svg width="8" height="5" viewBox="0 0 8 5" fill="none" stroke="#fff" stroke-width="1.4"><path d="M.5 4.5l3.5-3.5 3.5 3.5"/></svg>
    </div>
    <div class="task-list">
      <div class="task" style="top:9px">
        <div class="task-name">Finalise court documents</div>
        <div class="task-meta">
          <svg width="9" height="8" viewBox="0 0 9 8" fill="none" stroke="var(--accent)" stroke-width="1"><rect x=".5" y="2" width="8" height="5.5"/><path d="M3 2V.6h3V2M.5 4.5h8"/></svg>
          1157 Bramwell v. The State of ...<span class="date">23/05/18</span>
        </div>
      </div>
      <div class="task" style="top:49px">
        <div class="task-name">Finalise court settlement figures</div>
        <div class="task-meta">
          <svg width="9" height="8" viewBox="0 0 9 8" fill="none" stroke="var(--accent)" stroke-width="1"><rect x=".5" y="2" width="8" height="5.5"/><path d="M3 2V.6h3V2M.5 4.5h8"/></svg>
          R Tollander<span class="date">23/05/18</span>
        </div>
      </div>
      <div class="task" style="top:89px">
        <div class="task-name">Finalise court documents</div>
        <div class="task-meta">
          <svg width="9" height="8" viewBox="0 0 9 8" fill="none" stroke="var(--accent)" stroke-width="1"><rect x=".5" y="2" width="8" height="5.5"/><path d="M3 2V.6h3V2M.5 4.5h8"/></svg>
          1157 Bramwell v. The State of ...<span class="date">23/05/18</span>
        </div>
      </div>
    </div>
    <div class="accordion-head todo">To Do<span class="count">24</span>
      <svg width="8" height="5" viewBox="0 0 8 5" fill="none" stroke="#fff" stroke-width="1.4"><path d="M.5.5l3.5 3.5 3.5-3.5"/></svg>
    </div>
  </section>

  <section class="card time">
    <div class="card-title">My Time Records</div>
    <div class="stat" style="left:191px;width:49px"><div class="stat-label">Today</div><div class="stat-value">5h</div></div>
    <div class="stat" style="left:253px;width:73px"><div class="stat-label">This Week</div><div class="stat-value">24h 7m</div></div>
    <div class="stat" style="left:339px;width:79px"><div class="stat-label">This Month</div><div class="stat-value">56h 34m</div></div>
    <svg class="chart" width="436" height="311" viewBox="0 0 436 311" font-family="Signika, sans-serif" font-size="8" fill="#555">
      <g stroke="#e6e9ec" stroke-width="1">
        <path d="M36 90H418M36 114H418M36 138H418M36 162H418M36 186H418M36 210H418M36 234H418M36 258H418M36 282H418M36 90V282M418 90V282"/>
      </g>
      <g text-anchor="end">
        <text x="29" y="93">8h</text><text x="29" y="117">7h</text><text x="29" y="141">6h</text><text x="29" y="165">5h</text>
        <text x="29" y="189">4h</text><text x="29" y="213">3h</text><text x="29" y="237">2h</text><text x="29" y="261">1h</text>
      </g>
      <g fill="var(--brand)">
        <rect x="37" y="219.6" width="12" height="62.4"/><rect x="68.8" y="212.4" width="12" height="69.6"/>
        <rect x="100.7" y="186" width="12" height="96"/><rect x="132.5" y="202.8" width="12" height="79.2"/>
        <rect x="164.3" y="171.6" width="12" height="110.4"/><rect x="196.2" y="152.4" width="12" height="129.6"/>
        <rect x="228" y="183.6" width="12" height="98.4"/><rect x="259.8" y="169.2" width="12" height="112.8"/>
        <rect x="291.6" y="142.8" width="12" height="139.2"/><rect x="323.5" y="133.2" width="12" height="148.8"/>
        <rect x="355.3" y="154.8" width="12" height="127.2"/><rect x="387.1" y="126" width="12" height="156"/>
      </g>
      <g fill="var(--accent)">
        <rect x="50" y="202.8" width="12" height="79.2"/><rect x="81.8" y="198" width="12" height="84"/>
        <rect x="113.7" y="178.8" width="12" height="103.2"/><rect x="145.5" y="154.8" width="12" height="127.2"/>
        <rect x="177.3" y="142.8" width="12" height="139.2"/><rect x="209.2" y="133.2" width="12" height="148.8"/>
        <rect x="241" y="126" width="12" height="156"/><rect x="272.8" y="118.8" width="12" height="163.2"/>
        <rect x="304.6" y="114" width="12" height="168"/><rect x="336.5" y="104.4" width="12" height="177.6"/>
        <rect x="368.3" y="114" width="12" height="168"/><rect x="400.1" y="109.2" width="12" height="172.8"/>
      </g>
      <g text-anchor="middle">
        <text x="49.5" y="296">Jan</text><text x="81.3" y="296">Feb</text><text x="113.2" y="296">Mar</text>
        <text x="145" y="296">Apr</text><text x="176.8" y="296">May</text><text x="208.7" y="296">Jun</text>
        <text x="240.5" y="296">Jul</text><text x="272.3" y="296">Aut</text><text x="304.1" y="296">Sep</text>
        <text x="336" y="296">Oct</text><text x="367.8" y="296">Nov</text><text x="399.6" y="296">Dec</text>
      </g>
    </svg>
  </section>

  <section class="card matters">
    <div class="card-title">My Recent Matters</div>
    <div class="matter" style="top:45px">
      <svg width="9" height="8" viewBox="0 0 9 8" fill="none" stroke="var(--accent)" stroke-width="1"><rect x=".5" y="2" width="8" height="5.5"/><path d="M3 2V.6h3V2M.5 4.5h8"/></svg>
      <div><div class="matter-name">1157 Halvorsen v. Director of Public Prosecutions<br>concerning motor vehicle</div><div class="stamp">7 hours ago</div></div>
    </div>
    <div class="matter" style="top:92px">
      <svg width="9" height="8" viewBox="0 0 9 8" fill="none" stroke="var(--accent)" stroke-width="1"><rect x=".5" y="2" width="8" height="5.5"/><path d="M3 2V.6h3V2M.5 4.5h8"/></svg>
      <div><div class="matter-name">1157 Halvorsen v. Director of Public Prosecutions<br>concerning motor vehicle</div><div class="stamp">7 hours ago</div></div>
    </div>
    <div class="matter" style="top:139px">
      <svg width="9" height="8" viewBox="0 0 9 8" fill="none" stroke="var(--accent)" stroke-width="1"><rect x=".5" y="2" width="8" height="5.5"/><path d="M3 2V.6h3V2M.5 4.5h8"/></svg>
      <div><div class="matter-name">1157 Halvorsen v. Director of Public Prosecutions<br>concerning motor vehicle</div><div class="stamp">7 hours ago</div></div>
    </div>
    <div class="matter" style="top:186px">
      <svg width="9" height="8" viewBox="0 0 9 8" fill="none" stroke="var(--accent)" stroke-width="1"><rect x=".5" y="2" width="8" height="5.5"/><path d="M3 2V.6h3V2M.5 4.5h8"/></svg>
      <div><div class="matter-name">1157 Halvorsen v. Director of Public Prosecutions<br>concerning motor vehicle</div><div class="stamp">7 hours ago</div></div>
    </div>
  </section>

  <section class="card documents">
    <div class="card-title">My Recent Documents</div>
    <div class="document" style="top:42px">
      <svg width="11" height="12" viewBox="0 0 11 12" fill="none" stroke="#2e9e4f" stroke-width="1.1"><path d="M1 .6h6l3 3v7.8H1z"/><path d="M3.5 6h4M3.5 8.5h4"/></svg>
      <div><div class="matter-name">Document title goes here.xl</div><div class="stamp">1 hour ago</div></div>
    </div>
    <div class="document" style="top:79px">
      <svg width="11" height="12" viewBox="0 0 11 12" fill="none" stroke="#2b6cc4" stroke-width="1.1"><path d="M1 .6h6l3 3v7.8H1z"/><path d="M3.5 6h4M3.5 8.5h4"/></svg>
      <div><div class="matter-name">Document title goes here.doc</div><div class="stamp">1 hour ago</div></div>
    </div>
  </section>
</body>
</html>
```